WP website design (Carrowind)

We need a wordpress design for an established auction and real estate company based in Florida. The winning design will incorporate a professional color scheme with company logo in a clean layout. The design needs to consider that this will be developed on a responsive theme. Colors are those that will highlight the logo.

Industry/Entity Type

Real Estate

Font styles to use
Serif
Sans Serif

Colors

Designer to choose colors to be used in the design.

Requirements
Must have
• Navigation:
1) Home
2) Auctions
3) Online Auctions
4) About Us
5) Services
6) Real Estate Listings
7) References
8) Contact Us

Colors will be blue (#000066) / red (#B10000) and black or other complementary color. Tagline to be used "Since 1977, Proven Results." Slideshow to be placed in the header or body of home page - please use stock real estate image.

Widgets: 1) Email Sign-up 2) Social media icons for Chirpa and TradeLoop 3) Featured Listings 4) Testimonials 5) Register button

Footer will have smaller company logo, attached logos and contact info:
Phone: (555) 218-6049 Mobile: (555) 762-3815
Email: marlacarrowind@plexmail.example
Address: 48 E. Thornbury Lane, Ste 310, Pensacola, FL 32599
Nice to have
• Use of a drop down menu:
Auctions-
1) Upcoming Auctions
2) Past Auctions

```html
<!DOCTYPE html>
<html lang="en">
<head>
<meta charset="utf-8">
<title>Carrowind Auctions</title>
<link href="https://fonts.googleapis.com/css2?family=Arimo:ital,wght@0,400;0,700;1,400&family=Days+One&family=Michroma&display=swap" rel="stylesheet">
<style>
:root{
  --blue:#2e3192;
  --red:#d7212a;
  --dark:#3a3a3a;
  --text:#333333;
  --muted:#777777;
  --white:#ffffff;
  --badge:#6e6e6e;
}
*{box-sizing:border-box;margin:0;padding:0}
html,body{width:960px;height:1200px;overflow:hidden;background:var(--white)}
body{position:relative;font-family:"Arimo",Arial,sans-serif;color:var(--text)}
.abs{position:absolute}
.brand{left:88px;top:18px;display:flex;align-items:center;gap:12px}
.brand-mark{width:46px;height:46px;background:var(--blue)}
.brand-name{font-family:"Days One",sans-serif;font-size:34px;color:var(--blue);line-height:1}
.follow{right:88px;top:34px;display:flex;align-items:center;gap:12px;font-family:"Days One",sans-serif;font-size:14px;color:#444;letter-spacing:1px}
.social{display:flex;align-items:center;gap:5px;font-family:"Arimo",sans-serif;font-weight:700;font-size:12px;color:var(--blue);letter-spacing:0}
.social i{width:14px;height:14px;border-radius:50%;background:var(--blue);display:block}
.nav{left:86px;top:84px;width:788px;height:34px;background:var(--blue);border-radius:8px;display:flex;z-index:2}
.nav a{color:var(--white);text-decoration:none;font-weight:700;font-size:12.5px;display:flex;align-items:center;justify-content:center;border-right:1px solid rgba(255,255,255,.25)}
.nav a:last-child{border-right:none}
.hero{left:0;top:102px;width:960px;height:420px;background:linear-gradient(180deg,#5d86c6 0%,#9fb7d8 30%,#d9b38a 48%,#6c5a4e 62%,#2d62c4 78%,#1b2a48 100%)}
.welcome{left:88px;top:536px;display:flex;align-items:center;gap:10px}
.welcome i{width:28px;height:28px;background:var(--blue);display:block}
.welcome h1{font-family:"Days One",sans-serif;font-weight:400;font-size:25px;color:var(--blue)}
.intro{left:88px;top:579px;width:536px;font-size:10.5px;line-height:16px;letter-spacing:.2px}
.intro p+p{margin-top:32px}
.featured{left:88px;top:758px;font-family:"Days One",sans-serif;font-size:15px;color:var(--red);letter-spacing:1.5px}
.lot{width:520px}
.lot h3{font-family:"Michroma",sans-serif;font-weight:400;font-size:11px;letter-spacing:.8px;color:#222}
.lot .thumb{position:absolute;left:0;top:26px;width:132px;height:82px;border:1px solid #ddd;padding:3px}
.lot .thumb div{width:100%;height:100%;background:linear-gradient(180deg,#6f8fb8,#3b4a66 55%,#1e2a3c)}
.lot .info{position:absolute;left:141px;top:26px;width:380px;font-size:10px;line-height:16px;color:#222}
.lot .kind{color:var(--blue);font-size:11.5px;letter-spacing:.6px;margin-bottom:1px}
.lot .desc{line-height:14.5px;margin-top:3px}
.btns{position:absolute;right:0;top:114px;display:flex;gap:5px}
.btn{height:22px;border-radius:5px;color:var(--white);font-weight:700;font-size:10px;display:flex;align-items:center;gap:5px;padding:0 8px}
.btn.red{background:var(--red)}
.btn.black{background:#222}
.divider{left:84px;top:934px;width:504px;border-top:1px dotted #aaa}
.register{left:654px;top:538px;width:218px;height:50px;background:var(--red);border-radius:10px;display:flex;align-items:center;justify-content:center;gap:8px;color:var(--white);font-family:"Days One",sans-serif;font-size:22px;letter-spacing:1.5px}
.signup{left:654px;top:604px;width:218px;height:210px;background:var(--blue);border-radius:10px;padding:16px 13px}
.signup h2{font-family:"Michroma",sans-serif;font-weight:400;font-size:13px;color:var(--white);margin-bottom:14px;padding-left:2px}
.field{height:26px;background:var(--white);border-radius:4px;margin-bottom:8px;font-size:10.5px;color:#888;display:flex;align-items:center;padding-left:8px}
.subscribe{margin:20px auto 0;width:143px;height:26px;background:var(--red);color:var(--white);font-size:14px;display:flex;align-items:center;justify-content:center;letter-spacing:.5px}
.testi{left:654px;top:836px;width:220px;height:170px;background:var(--red);border-radius:12px;padding:10px 13px;color:var(--white)}
.testi h2{font-family:"Michroma",sans-serif;font-weight:400;font-size:14px;margin-bottom:8px}
.testi p{font-style:italic;font-size:9.6px;line-height:14.4px;text-align:justify}
.author{right:158px;top:1046px;text-align:right;font-style:italic;font-size:9.5px;line-height:16px}
.author small{color:var(--muted);font-size:8px}
.avatar{left:813px;top:1037px;width:47px;height:40px;border:1px solid #ccc;background:linear-gradient(180deg,#b58f6c,#6e4b35)}
.footer{left:0;top:1103px;width:960px;height:72px;background:var(--dark)}
.fbrand{left:94px;top:20px;display:flex;align-items:center;gap:8px;font-family:"Days One",sans-serif;font-size:18px;color:#e8e8e8}
.fbrand i{width:32px;height:32px;background:#e8e8e8;display:block}
.badge{top:18px;height:36px;background:var(--badge);border-radius:4px}
.bar{left:0;top:1175px;width:960px;height:25px;background:var(--red);color:var(--white);font-size:10.2px;display:flex;align-items:center;justify-content:center;gap:10px}
</style>
</head>
<body>
<header>
  <div class="abs brand"><i class="brand-mark"></i><span class="brand-name">Carrowind</span></div>
  <div class="abs follow">Follow us on
    <span class="social"><i></i>TradeLoop</span>
    <span class="social"><i></i>Chirpa</span>
  </div>
  <nav class="abs nav">
    <a style="width:68px">Home</a><a style="width:85px">Auctions</a><a style="width:126px">Online Auctions</a><a style="width:89px">About Us</a><a style="width:81px">Services</a><a style="width:148px">Real Estate Listings</a><a style="width:97px">References</a><a style="width:94px">Contact Us</a>
  </nav>
  <div class="abs hero" role="img" aria-label="Photo of a modern house with lit interiors and a blue pool at dusk"></div>
</header>

<main>
  <div class="abs welcome"><i></i><h1>Welcome to Carrowind</h1></div>
  <div class="abs intro">
    <p><b>Carrowind Auction</b> is simply dummy text of the printing and typesetting industry. Lorem Ipsum has been the industry's standard dummy text ever since the 1500s, when an unknown printer took a galley of type and scrambled it to make a type specimen book. It has survived not only five centuries, but also the leap into electronic typesetting, remaining essentially unchanged. It has survived not only five centuries, but also the leap into electronic typesetting, remaining essentially unchanged.</p>
    <p>It was popularised in the 1960s with the release of Typeforge sheets containing Lorem Ipsum passages, and more recently Typeforge sheets containing Lorem Ipsum passages, and more recently containing Lorem Ipsum passages, and more recently</p>
  </div>
  <h2 class="abs featured">FEATURED AUCTIONS</h2>

  <article class="abs lot" style="left:88px;top:793px;height:132px">
    <h3>SHOP EQUIPMENT/TOOLS * PORK PROCESSING ITEMS</h3>
    <div class="thumb"><div role="img" aria-label="Photo of a modern two-storey house at night"></div></div>
    <div class="info">
      <div class="kind">LIVE ON-SITE AUCTION</div>
      <div><b>Begins:</b>&nbsp; Saturday, March 16, 2013 at 10:00 AM EDT</div>
      <div><b>Location:</b>&nbsp; 2958 Merrow Road Bagdad, KY 40099</div>
      <div class="desc">Kestrel BS3F High Lift, 600 Series Halden tractor w/Brantley Loader, Dune buggy, 1207 HT Cutditioner: SHOP.</div>
    </div>
    <div class="btns"><span class="btn red">&#9632;&#8801; Details</span><span class="btn black">&#9998; Details</span></div>
  </article>
  <div class="abs divider"></div>
  <article class="abs lot" style="left:94px;top:952px;height:132px">
    <h3>SHOP EQUIPMENT/TOOLS * PORK PROCESSING ITEMS</h3>
    <div class="thumb"><div role="img" aria-label="Photo of a modern two-storey house at night"></div></div>
    <div class="info">
      <div class="kind">LIVE ON-SITE AUCTION</div>
      <div><b>Begins:</b>&nbsp; Saturday, March 16, 2013 at 10:00 AM EDT</div>
      <div><b>Location:</b>&nbsp; 2958 Merrow Road Bagdad, KY 40099</div>
      <div class="desc">Kestrel BS3F High Lift, 600 Series Halden tractor w/Brantley Loader, Dune buggy, 1207 HT Cutditioner: SHOP.</div>
    </div>
    <div class="btns"><span class="btn red">&#9632;&#8801; Details</span><span class="btn black">&#9998; Details</span></div>
  </article>
</main>

<aside>
  <div class="abs register">
    <svg width="38" height="38" viewBox="0 0 38 38" fill="none" stroke="#fff" stroke-width="3"><rect x="3" y="7" width="24" height="27" rx="2"/><path d="M9 20l6 6 17-19"/></svg>
    REGISTER
  </div>
  <form class="abs signup">
    <h2>Email Sign Up Form</h2>
    <div class="field">First Name</div>
    <div class="field">Last Name</div>
    <div class="field">Email Address</div>
    <span class="subscribe">Subscribe Now</span>
  </form>
  <div class="abs testi">
    <h2>Testimonials</h2>
    <p>Ipsum is simply dummy text of the printing and typesetting industry. Lorem Ipsum has been the industry's standard dummy text ever since the 1500s, when an unknown printer took a galley of type and scrambled it to make a type specimen book. It has survived not only five centuries, but also the leap into electronic typesetting,</p>
  </div>
  <svg class="abs" style="left:810px;top:1004px" width="24" height="30" viewBox="0 0 24 30"><path d="M0 0h22l2 30z" fill="#d7212a"/></svg>
  <div class="abs author">By Dale Prewitt<br><small>Posted on Nov25, 2012</small></div>
  <div class="abs avatar" role="img" aria-label="Portrait photo of the reviewer"></div>
</aside>

<footer>
  <div class="abs footer">
    <div class="abs fbrand"><i></i>Carrowind</div>
    <span class="abs badge" style="left:266px;width:52px"></span>
    <span class="abs badge" style="left:332px;width:30px"></span>
    <span class="abs badge" style="left:374px;width:126px"></span>
    <span class="abs badge" style="left:505px;width:65px"></span>
    <span class="abs badge" style="left:596px;width:150px"></span>
    <span class="abs badge" style="left:764px;width:106px"></span>
  </div>
  <div class="abs bar">
    <span>Phone: (555) 218-6049</span>|<span>Mobile: (555) 762-3815</span>|<span>Email: marlacarrowind@plexmail.example</span>|<span>Address: 48 E. Thornbury Lane, Ste 310, Pensacola, FL 32599</span>
  </div>
</footer>
</body>
</html>
```